Out Door Living brochure

We need a Great looking brochure to feature the latest in out door living. Showcasing out doors is the new living space.

I'm enclosing our logo and a brochure we had done recently it didn't have enough impact. This one was a single fold you can also provide a tri fold if you see fit. We like the verbiage, but if you can spice it up we would love to see that. This brochure will be added to our sales packet.
Thank you!!!

Target Market(s)

Home owners

Industry/Entity Type

Construction Company

Logo Text

(See logo) Beautiful Homes Built to Last Introducing Outdoor living 2017

Font styles to use
Serif

Requirements
Must have
• Logo and
• Beautiful Homes Built to Last
• Introducing Outdoor living 2017
Nice to have
• Benefits of outdoor living
Should not have
• Bad photos if these don't work let me know we can get others to replace the sapce

```html
<!DOCTYPE html>
<html lang="en">
<head>
<meta charset="utf-8">
<title>Harbor Ridge Builders – Outdoor Living 2017 Trifold</title>
<link href="https://fonts.googleapis.com/css2?family=Open+Sans:wght@400;600;700&family=Roboto+Slab:wght@400;700&display=swap" rel="stylesheet">
<style>
  :root{
    --sky:#4fb3e8;
    --sky-light:#7fcdf2;
    --slate:#4b6277;
    --slate-dark:#3c5165;
    --paper:#efefef;
    --ink:#1f2a33;
    --cover-blue:#6f93b5;
    --stage:#f4f5f6;
    --white:#ffffff;
  }
  *{box-sizing:border-box;margin:0;padding:0}
  html,body{width:1011px;height:1200px;overflow:hidden;background:var(--stage)}
  body{font-family:"Open Sans",Arial,sans-serif;color:var(--ink);position:relative}
  .spread{position:absolute;left:135px;width:740px;height:572px;background:var(--paper);overflow:hidden;box-shadow:0 6px 24px rgba(0,0,0,.18)}
  .spread--outside{top:20px}
  .spread--inside{top:608px}
  .panel{position:absolute;top:0;height:572px;width:247px;overflow:hidden}
  .panel--1{left:0}.panel--2{left:247px}.panel--3{left:494px;width:246px}
  .photo{position:absolute}
  .fold{position:absolute;top:0;width:1px;height:100%;background:rgba(0,0,0,.08)}

  /* outside left panel */
  .tagline{position:absolute;left:22px;top:210px;width:200px;font-size:13px;line-height:1.35;font-style:italic;color:#444}
  .band{position:absolute;background:var(--slate);color:var(--white)}
  .band--staycation{left:0;top:280px;width:247px;height:82px;padding:10px 16px;font-family:"Roboto Slab",Georgia,serif;font-weight:700;font-style:italic;font-size:16px;line-height:1.25}

  /* contact panel */
  .brand{display:flex;align-items:center;gap:8px;font-family:"Open Sans",Arial,sans-serif;font-weight:600;letter-spacing:.08em;text-transform:uppercase;color:var(--slate);white-space:nowrap}
  .brand__mark{width:14px;height:14px;background:var(--sky);flex:none}
  .brand--contact{position:absolute;left:28px;top:268px;font-size:12.5px}
  .contact{position:absolute;left:28px;top:320px;width:200px;font-size:12.5px;line-height:1.55;color:var(--ink)}
  .contact__phone{font-family:"Roboto Slab",Georgia,serif;font-weight:700;font-size:21px;color:var(--sky);display:flex;align-items:center;gap:6px;margin-bottom:4px}
  .contact__row{display:flex;gap:7px;align-items:flex-start;overflow-wrap:anywhere}
  .contact__row svg{flex:none;margin-top:3px}

  /* cover */
  .cover{background:var(--cover-blue)}
  .brand--cover{position:absolute;left:36px;top:90px;font-size:12.5px;color:var(--slate-dark)}
  .cover__intro{position:absolute;left:28px;top:232px;font-family:"Roboto Slab",Georgia,serif;font-size:27px;color:var(--white)}
  .cover__title{position:absolute;left:28px;top:270px;font-family:"Roboto Slab",Georgia,serif;font-weight:700;font-size:35px;line-height:1.05;color:var(--sky-light)}
  .band--cover{left:0;top:362px;width:246px;height:36px;background:var(--slate-dark);font-family:"Roboto Slab",Georgia,serif;font-weight:700;font-size:14px;line-height:36px;text-align:center}

  /* inside */
  .band--evolved{left:0;top:28px;width:247px;height:150px;background:var(--slate)}
  .headline{background:var(--sky);color:var(--white);font-family:"Roboto Slab",Georgia,serif;font-weight:700;font-size:14px;line-height:1.15;text-align:center;text-transform:uppercase;padding:6px 8px;margin-top:4px}
  .band--evolved p{font-size:11.5px;line-height:1.4;padding:10px 16px}
  .band--oasis{left:0;top:372px;width:246px;height:200px;padding:40px 20px;font-family:"Roboto Slab",Georgia,serif;font-weight:700;font-size:17px;line-height:1.3;text-align:center}
</style>
</head>
<body>

<section class="spread spread--outside">
  <div class="panel panel--1">
    <div class="photo" role="img" aria-label="Stone water feature with palm planter on a patio" style="left:0;top:0;width:247px;height:195px;background:linear-gradient(160deg,#8fa3ae,#4d5d66 60%,#6e7d84)"></div>
    <p class="tagline">Innovative ideas that help stretch out the seasons, making it comfy and cozy.</p>
    <div class="band band--staycation">Enjoy your staycation in the comfort of your own back yard.</div>
    <div class="photo" role="img" aria-label="Stone fire pit under a covered patio" style="left:0;top:362px;width:247px;height:210px;background:linear-gradient(170deg,#c9c3bb,#6f655b 55%,#3e3a36)"></div>
  </div>

  <div class="panel panel--2">
    <div class="photo" role="img" aria-label="White water lily in bloom" style="left:0;top:0;width:247px;height:230px;background:radial-gradient(circle at 50% 55%,#f6f2ea,#c9c3b6 45%,#5e6a58)"></div>
    <div class="brand brand--contact"><span class="brand__mark"></span>Harbor Ridge Builders</div>
    <div class="contact">
      <div class="contact__phone">
        <svg width="14" height="18" viewBox="0 0 14 18"><path d="M3 1 L6 1 L7 5 L5 6.5 Q6.5 10.5 9 12.5 L11 11 L13.5 13 L13 16.5 Q4 17 1.5 6 Q1 2 3 1Z" fill="#1f2a33"/></svg>
        555-014-0392
      </div>
      <div class="contact__row"><svg width="13" height="10" viewBox="0 0 13 10"><rect x=".5" y=".5" width="12" height="9" fill="none" stroke="#1f2a33"/><path d="M.5 .5 L6.5 5.5 L12.5 .5" fill="none" stroke="#1f2a33"/></svg>sam.reyes@example.net</div>
      <div class="contact__row"><svg width="12" height="12" viewBox="0 0 12 12"><circle cx="6" cy="6" r="5.5" fill="none" stroke="#1f2a33"/><ellipse cx="6" cy="6" rx="2.3" ry="5.5" fill="none" stroke="#1f2a33"/><path d="M.5 6 H11.5" stroke="#1f2a33"/></svg>www.harborridge.example</div>
      <div class="contact__row"><svg width="10" height="13" viewBox="0 0 10 13"><path d="M5 12.5 Q0.5 7 0.5 4.8 A4.5 4.5 0 0 1 9.5 4.8 Q9.5 7 5 12.5Z" fill="#1f2a33"/><circle cx="5" cy="4.8" r="1.6" fill="#efefef"/></svg>1480 Alder Crest Way,<br>Bayview, CA 94000</div>
    </div>
    <svg class="photo" style="left:0;top:520px" width="247" height="52" viewBox="0 0 247 52"><path d="M0 8 Q120 52 247 40 L247 52 L0 52Z" fill="#4fb3e8"/></svg>
  </div>

  <div class="panel panel--3 cover">
    <div class="photo" role="img" aria-label="Covered outdoor kitchen on a deck, tinted blue" style="left:0;top:0;width:246px;height:572px;background:linear-gradient(180deg,#7b9dbd,#5f84a8 55%,#7096b8)"></div>
    <div class="brand brand--cover"><span class="brand__mark"></span>Harbor Ridge Builders</div>
    <div class="cover__intro">Introducing</div>
    <div class="cover__title">Outdoor<br>Living 2017</div>
    <div class="band band--cover">Beautiful Homes Built to Last</div>
  </div>
  <span class="fold" style="left:247px"></span><span class="fold" style="left:494px"></span>
</section>

<section class="spread spread--inside">
  <div class="panel panel--1">
    <div class="band band--evolved">
      <div class="headline">The Outdoor Experience<br>Has Evolved</div>
      <p>It used to be a gas grill, tables and a few chairs. Now we have whole kitchens, outdoors fireplaces, and waterproof electronics to extend the season.</p>
    </div>
    <div class="photo" role="img" aria-label="Poolside dining set under a pergola with palm trees" style="left:0;top:178px;width:247px;height:245px;background:linear-gradient(180deg,#8fb6cf,#6b7570 45%,#4a4036)"></div>
    <svg class="photo" style="left:0;top:410px" width="247" height="40" viewBox="0 0 247 40"><path d="M0 30 Q150 0 247 10 L247 18 Q150 8 0 40Z" fill="#ffffff"/></svg>
    <div class="photo" role="img" aria-label="Planter with flowers beside a blue pool" style="left:0;top:432px;width:247px;height:140px;background:linear-gradient(160deg,#7a8a6a,#2b6f95 55%,#1f5a80);clip-path:polygon(0 18%,60% 0,100% 4%,100% 100%,0 100%)"></div>
  </div>

  <div class="panel panel--2">
    <div class="photo" role="img" aria-label="Lit outdoor lounge with stone wall" style="left:0;top:0;width:247px;height:160px;background:linear-gradient(160deg,#d8c7ad,#8a6f52 50%,#4a3a2c)"></div>
    <div class="photo" role="img" aria-label="Outdoor kitchen with stainless grill and bar seating" style="left:0;top:160px;width:493px;height:250px;background:linear-gradient(100deg,#6b8d8f,#5a6a6b 40%,#a9c3cd 75%,#8fb3c6)"></div>
    <div class="photo" role="img" aria-label="Outdoor bar at night with blue stools" style="left:0;top:410px;width:247px;height:162px;background:linear-gradient(170deg,#3a2e22,#6a4a2a 50%,#1f5f7a)"></div>
  </div>

  <div class="panel panel--3">
    <div class="photo" role="img" aria-label="Stacked stone fire pit" style="left:0;top:14px;width:246px;height:130px;background:linear-gradient(160deg,#9a8e80,#5c5248 60%,#3e3833);border:6px solid #ffffff"></div>
    <div class="photo" role="img" aria-label="Outdoor kitchen bar with blue stools and glass railing" style="left:0;top:150px;width:246px;height:222px;background:linear-gradient(100deg,#8fb3c6,#c9dbe3 50%,#6aa8c8)"></div>
    <div class="band band--oasis">Transform your outdoor space into an oasis you may never want to leave.</div>
  </div>
  <span class="fold" style="left:247px"></span><span class="fold" style="left:494px"></span>
</section>

</body>
</html>
```